Velmorytrips.com web design project + logo design

Hi,

We are a Russian online tour operator - roamquiltex.com

We are looking to tranmsfer our domain to velmorytrips.com. The website and logo need to be velmoryesque - we are not looking to change our functionality, but we need to make the website much more attracitve to clients, much more wild looking but at the same time remaining a professional travel company.

The main concept of the website should be innovative travel (as velmory was an innovator). Alternatively, you could go down the artist route and go down the draw / design your own tour road.

On our website the customer is able to combine travel services (hotels, flights, Visa services, and soon chauffeur, car rental etc...) put it into their basket (the basket definitely has to look better than it is at the moment) and pay for it in one go by card.

We are also stressin our customer support with web chat, call centre etc... (call centre number at the top of the page)

We aim to provide an easy user experience, but we need to make it have some more style, so I will be waiting for what you guys can come up with.
Let me know if you have any questions - skype is: mrkostelin

Industry/Entity Type

It Company

Logo Text

Requirements
Must have
• It is quite a simple task - to take the existing website roamquiltex.com and velmorysize it to create velmorytrips.com, the functionality of the website will remain the same and there are not many pages in the website. Homepage, Checkout step1, Checkout step 2 (you can view both of these if you select a service) and the generic pages for T&C''s, Privacy policy etc...

IMPORTANT UPDATE

We are also looking at how the search results will look in the designs, (please do a search on our website for hotel / flight)

```html
<!DOCTYPE html>
<html lang="ru">
<head>
<meta charset="utf-8">
<title>Velmory Travel</title>
<link href="https://fonts.googleapis.com/css2?family=Open+Sans:wght@400;600;700&family=Arimo:wght@400;700&display=swap" rel="stylesheet">
<style>
:root{
  --sky-top:#c9ced6;
  --sky-mid:#e3e5e9;
  --sky-low:#d2d4d8;
  --fortress:#8a6a3c;
  --fortress-dark:#4a3a22;
  --footer:#2a2520;
  --white:#ffffff;
  --panel-line:#e2e2e2;
  --text:#5a5a5a;
  --text-dark:#333333;
  --muted:#8c8c8c;
  --red:#d2232a;
  --orange:#eea200;
  --orange-deep:#d46c10;
  --purple:#a548b5;
  --green:#3ea51e;
  --field:#f5f5f5;
  --field-line:#d4d4d4;
  --btn-dark:#3a3a3a;
}
*{box-sizing:border-box;margin:0;padding:0}
html,body{width:1022px;height:1200px;overflow:hidden}
body{position:relative;font-family:"Arimo",Arial,sans-serif;color:var(--text);
  background:linear-gradient(180deg,var(--sky-top) 0,var(--sky-mid) 300px,var(--sky-low) 900px,#b8a78c 990px,var(--fortress) 1060px,var(--fortress-dark) 1133px)}
.abs{position:absolute}
.landscape{left:0;top:960px;width:1022px;height:173px;background:linear-gradient(180deg,rgba(150,130,100,0) 0,#9a7846 60%,#5b4628 100%)}
.brand{left:76px;top:28px;font-family:"Open Sans",sans-serif;font-weight:700;font-size:17px;line-height:20px;color:#222;letter-spacing:1px;text-align:center}
.brand-mark{width:14px;height:14px;background:var(--purple);margin:0 auto 6px}
.contacts{right:75px;top:14px;text-align:right;font-family:"Open Sans",sans-serif}
.contacts .phone-main{font-size:19px;color:var(--red);line-height:26px}
.contacts .phone-alt{font-size:15px;color:var(--red);line-height:25px}
.contacts .hours{font-size:15px;color:#333;line-height:25px}
.slide{border:4px solid var(--white);box-shadow:0 2px 8px rgba(0,0,0,.25)}
.slide-left{left:116px;top:135px;width:223px;height:243px;background:linear-gradient(180deg,#9aa0a6,#5e5a52 60%,#3b3a36)}
.slide-right{left:683px;top:135px;width:224px;height:243px;background:linear-gradient(180deg,#8ea9c8,#a9b9c4 30%,#6f8f58 55%,#4d7a2c)}
.slide-center{left:339px;top:109px;width:344px;height:269px;background:linear-gradient(180deg,#9db7d6,#c9d4de 35%,#b86a4a 65%,#5d6b3d);z-index:2}
.caption{left:0;right:0;bottom:0;height:74px;background:rgba(20,20,20,.72);padding:10px 20px;color:#fff}
.caption h3{font-family:"Open Sans",sans-serif;font-size:12.5px;font-weight:700;margin-bottom:6px}
.caption p{font-size:11px;line-height:16px}
.arrow{width:28px;height:28px;border-radius:50%;background:#fff;border:1px solid #cfcfcf;display:flex;align-items:center;justify-content:center}
.panel-main{left:76px;top:376px;width:639px;height:637px;background:var(--white)}
.panel-side{left:715px;top:376px;width:230px;height:500px;background:var(--white)}
.nav{left:80px;top:378px;width:861px;height:44px;display:flex;align-items:center;background:#fafafa;border-bottom:1px solid var(--panel-line)}
.nav a{font-size:13px;color:#333;text-decoration:none;height:44px;display:flex;align-items:center;justify-content:center;border-right:1px solid var(--panel-line);gap:8px}
.nav a.active{color:var(--purple);background:#fff}
.lang{left:857px;top:387px;width:73px;height:24px;border:1px solid #ccc;background:#fff;font-size:10px;color:#333;display:flex;align-items:center;padding-left:8px;gap:6px}
.flag{width:14px;height:9px;background:linear-gradient(135deg,#2a3f8f,#c8102e 50%,#2a3f8f)}
.cart{left:88px;top:432px;width:613px;height:47px;border:1px solid #d8d8d8;border-radius:3px;background:linear-gradient(180deg,#fafafa,#e6e6e6);display:flex;align-items:center;padding-left:14px}
.cart-icon{width:34px;height:28px;background:linear-gradient(180deg,#9ad04a,#4f9a1a);border-radius:3px 3px 8px 8px}
.cart-title{font-family:"Open Sans",sans-serif;font-size:15px;font-weight:600;color:#333;margin-left:14px}
.cart-state{font-size:13px;color:#777;margin-left:26px}
.checkout{position:absolute;right:12px;top:9px;width:110px;height:27px;border-radius:14px;background:linear-gradient(180deg,#ffc21a,#f09a00);color:#fff;font-family:"Open Sans",sans-serif;font-size:12.5px;font-weight:700;display:flex;align-items:center;padding-left:14px}
.checkout span{position:absolute;right:5px;top:5px;width:17px;height:17px;border-radius:50%;background:#fff;display:flex;align-items:center;justify-content:center}
.service{top:491px;width:196px;height:196px;border:1px solid #e4e4e4;background:#f8f8f8;box-shadow:inset 0 0 0 4px #fff;padding:12px 12px}
.service-head{display:flex;align-items:center;gap:10px;height:44px;margin-bottom:14px}
.service-head h2{font-family:"Open Sans",sans-serif;font-size:19px;font-weight:600}
.service-icon{width:38px;height:38px;border-radius:4px}
.service p{font-size:11.5px;line-height:17.8px;text-align:justify}
.service .links{margin-top:8px;font-size:12px;line-height:16.5px;color:var(--orange-deep)}
.service .links li{list-style:none;margin-bottom:8px}
.visa h2{color:var(--orange)}
.air h2{color:var(--purple)}
.hotel h2{color:var(--green)}
.about{left:88px;top:708px;width:613px}
.about h2{font-family:"Open Sans",sans-serif;font-weight:600;font-size:18px;color:var(--orange);margin-bottom:4px}
.about p{font-size:12.5px;line-height:19.6px;text-align:justify}
.divider{left:88px;top:869px;width:613px;height:1px;background:var(--panel-line)}
.block-title{font-family:"Open Sans",sans-serif;font-size:15px;color:#333}
.input{width:194px;height:24px;border:1px solid #ccc;background:var(--field);font-size:10.5px;color:#333;display:flex;align-items:center;padding-left:14px}
.btn-gray{width:61px;height:26px;background:linear-gradient(180deg,#999,#6b6b6b);color:#fff;font-size:13px;font-weight:700;display:flex;align-items:center;justify-content:center;border-radius:2px}
.pay-name{font-family:"Open Sans",sans-serif;font-weight:700;font-size:24px;color:#1f5aa8}
.card{width:28px;height:15px;border-radius:2px}
.gallery-img{left:490px;top:911px;width:210px;height:84px;border:3px solid #ddd;background:linear-gradient(180deg,#7fa3cc,#b9c6d2 45%,#8a9a7a 70%,#4a6a32)}
.tabs{left:740px;top:450px;display:flex;gap:24px;font-size:12px}
.tabs .t-air{color:var(--orange);border-bottom:2px solid var(--orange);padding-bottom:3px}
.tabs .t-visa{color:var(--purple)}
.tabs .t-hotel{color:var(--green)}
.label{font-size:11px;color:#444}
.field{height:27px;border:1px solid var(--field-line);background:#fafafa;box-shadow:inset 0 0 0 2px #fff;font-size:9.5px;font-style:italic;color:#999;display:flex;align-items:center;padding-left:10px;justify-content:space-between;padding-right:10px}
.field.plain{font-style:normal}
.caret{width:0;height:0;border-left:5px solid transparent;border-right:5px solid transparent;border-top:5px solid #999}
.cal{width:16px;height:16px;border:1px solid #888;border-top:4px solid #666;background:#fff}
.btn-dark{left:849px;top:820px;width:74px;height:27px;background:linear-gradient(180deg,#555,#222);color:#fff;font-size:12.5px;display:flex;align-items:center;justify-content:center;border-radius:2px}
.footer{left:0;top:1133px;width:1022px;height:67px;background:rgba(30,26,22,.9)}
.footer-nav{left:76px;top:1148px;font-size:12px;color:#d8d0c4;word-spacing:2px}
.footer-nav span{color:#a69c8e;margin:0 7px}
.copyright{left:76px;top:1174px;font-size:12px;color:#c8c0b4}
.social{top:1160px;width:20px;height:20px;border-radius:3px}
</style>
</head>
<body>
<div class="abs landscape" role="img" aria-label="Evening panorama of a hilltop fortress and old town"></div>

<div class="abs brand"><div class="brand-mark"></div>VELMORY<br>TRAVEL</div>

<div class="abs contacts">
  <div class="phone-main">8-800-555-4126</div>
  <div class="phone-alt">+7 (495) 610-42-58</div>
  <div class="hours">(Пн-Пт) Часы работы: с <b>9:00</b> - до <b>18:00</b></div>
</div>

<div class="abs slide slide-left" role="img" aria-label="Cathedral with golden domes"></div>
<div class="abs slide slide-right" role="img" aria-label="Green valley with a lake and mountains"></div>
<div class="abs slide slide-center" role="img" aria-label="Colourful onion-domed cathedral under a blue sky">
  <div class="abs caption">
    <h3>Suspendisse cursus</h3>
    <p>Suspendisse ultricies sed neque et malesuada. Cras bibendum nec neque et adipiscing.</p>
  </div>
</div>
<div class="abs arrow" style="left:78px;top:230px"><svg width="8" height="12"><path d="M6 1 1 6l5 5" fill="none" stroke="#777" stroke-width="1.5"/></svg></div>
<div class="abs arrow" style="left:918px;top:230px"><svg width="8" height="12"><path d="M2 1l5 5-5 5" fill="none" stroke="#777" stroke-width="1.5"/></svg></div>

<div class="abs panel-main"></div>
<div class="abs panel-side"></div>

<nav class="abs nav">
  <a class="active" style="width:67px">Home</a>
  <a style="width:70px">About</a>
  <a style="width:83px">Services</a>
  <a style="width:73px">Places</a>
  <a style="width:59px">Visa</a>
  <a style="width:71px">Hotels</a>
  <a style="width:98px">Contact us</a>
  <a style="width:135px"><svg width="24" height="18"><path d="M2 2h13v9H7l-4 3v-3H2z" fill="#666"/><path d="M17 6h5v8h-1v3l-3-3h-6v-1h5z" fill="#888"/></svg>Forums</a>
  <a style="width:123px"><svg width="20" height="20"><circle cx="10" cy="6" r="5" fill="#555"/><path d="M1 20c0-6 4-8 9-8s9 2 9 8z" fill="#555"/></svg>My Tour</a>
</nav>
<div class="abs lang"><span class="flag" role="img" aria-label="English language flag"></span>Eng<span class="caret" style="margin-left:6px;border-top-color:#333"></span></div>

<div class="abs cart">
  <div class="cart-icon" role="img" aria-label="Shopping basket"></div>
  <div class="cart-title">Корзина :</div>
  <div class="cart-state">пусто</div>
  <div class="checkout">CHECKOUT<span><svg width="6" height="8"><path d="M0 0l6 4-6 4z" fill="#f09a00"/></svg></span></div>
</div>

<section class="abs service visa" style="left:88px">
  <div class="service-head">
    <svg width="38" height="36"><path d="M19 1 37 35H1z" fill="#f6b400" stroke="#e08a00"/><rect x="17" y="11" width="4" height="14" fill="#fff"/><rect x="17" y="28" width="4" height="4" fill="#fff"/></svg>
    <h2>ВИЗЫ</h2>
  </div>
  <p style="text-align:left">Aenean sit amet dapibus tellus Nullam sodales ante velit, nec Aliquam ultricies at felis.</p>
  <ul class="links"><li>1.Оформление визы «Онлайн»</li><li>2. Оформление визы «Самостоятельно».</li></ul>
</section>
<section class="abs service air" style="left:296px">
  <div class="service-head">
    <div class="service-icon" role="img" aria-label="Airplane over a ticket" style="background:linear-gradient(135deg,#7ec3e8,#3a7fc0)"></div>
    <h2>АВИАБИЛЕТЫ</h2>
  </div>
  <p>На нашем сайте вы можете рассматривать предложения от разных авиалиний и приобрести авиабилеты согласно вашим пожеланиям и бюджету. Планируйте даты отправлений и</p>
</section>
<section class="abs service hotel" style="left:504px">
  <div class="service-head">
    <div class="service-icon" role="img" aria-label="Hotel building" style="background:linear-gradient(180deg,#8fc0e8,#3f7fb8)"></div>
    <h2>ОТЕЛИ</h2>
  </div>
  <p>На нашем сайте вы можете рассматривать предложения от разных авиалиний и приобрести авиабилеты согласно вашим пожеланиям и бюджету. Планируйте даты отправлений и</p>
</section>

<section class="abs about">
  <h2>About Velmory Travel</h2>
  <p>Aenean vel tempus elit. Donec mattis bibendum consequat. Integer id mi suscipit urna vehicula blandit viverra nec nibh. Aliquam adipiscing libero eget tellus malesuada porttitor. Cras consectetur aliquam luctus. In blandit orci sapien, in eleifend ante lobortis vitae. Ut volutpat euismod leo, et sollicitudin lorem malesuada luctus. Morbi semper tempus diam, eget ultricies purus facilisis a. Pellentesque ullamcorper risus eget arcu dapibus, eu rhoncus mauris luctus. Quisque a odio at neque pellentesque placerat. Sed quis volutpat erat. Ut posuere quam consectetur scelerisque dapibus. Aenean scelerisque vehicula urna.</p>
</section>
<div class="abs divider"></div>

<div class="abs block-title" style="left:89px;top:881px">Email Signup</div>
<div class="abs input" style="left:89px;top:910px">Name</div>
<div class="abs input" style="left:89px;top:940px">Email ID</div>
<div class="abs btn-gray" style="left:222px;top:972px">SUBMIT</div>

<div class="abs block-title" style="left:331px;top:881px">Payments</div>
<div class="abs pay-name" style="left:338px;top:906px">PayQuill</div>
<div class="abs" style="left:332px;top:946px;display:flex;gap:3px">
  <div class="card" style="background:#e8edf5;border:1px solid #b8c4d8"></div>
  <div class="card" style="background:#f3e6d8;border:1px solid #d8b898"></div>
  <div class="card" style="background:#dde8f3;border:1px solid #a8c0dc"></div>
  <div class="card" style="background:#f0ebe4;border:1px solid #cfc3b3"></div>
</div>

<div class="abs block-title" style="left:490px;top:881px">Gallery</div>
<svg class="abs" style="left:690px;top:885px" width="10" height="12"><path d="M2 1l6 5-6 5" fill="none" stroke="#666" stroke-width="2"/></svg>
<div class="abs gallery-img" role="img" aria-label="White monastery with silver domes among trees"></div>

<div class="abs tabs"><span class="t-air">АВИАБИЛЕТЫ</span><span class="t-visa">ВИЗЫ</span><span class="t-hotel">ОТЕЛИ</span></div>
<svg class="abs" style="left:773px;top:469px" width="10" height="6"><path d="M0 0h10L5 6z" fill="#eea200"/></svg>

<div class="abs label" style="left:739px;top:490px">Откуда</div>
<div class="abs field" style="left:739px;top:507px;width:186px">Select<span class="caret"></span></div>
<div class="abs label" style="left:739px;top:544px">Куда</div>
<div class="abs field" style="left:739px;top:562px;width:186px">Select<span class="caret"></span></div>
<div class="abs label" style="left:739px;top:598px">Туда</div>
<div class="abs field" style="left:739px;top:616px;width:186px">dd/mm/yyyy<span class="cal"></span></div>
<div class="abs label" style="left:739px;top:653px">Обратно</div>
<div class="abs field" style="left:739px;top:670px;width:186px">dd/mm/yyyy<span class="cal"></span></div>
<div class="abs label" style="left:741px;top:707px">Пассажиры</div>
<div class="abs field plain" style="left:740px;top:724px;width:88px">Adults : 2<span class="caret"></span></div>
<div class="abs field plain" style="left:836px;top:724px;width:88px">Kids : 2<span class="caret"></span></div>
<div class="abs label" style="left:739px;top:763px">Класс</div>
<div class="abs field plain" style="left:739px;top:780px;width:186px;justify-content:flex-start;gap:16px">First class<span class="caret"></span></div>
<div class="abs btn-dark">SUBMIT</div>

<footer class="abs footer"></footer>
<div class="abs footer-nav">Home<span>|</span>About<span>|</span>Services<span>|</span>Places<span>|</span>Visa<span>|</span>Hotels<span>|</span>Contact us<span>|</span>Forums<span>|</span>My Tour</div>
<div class="abs copyright">Copyright &copy; 2013 &nbsp; www.roamquiltex.com &nbsp; All rights reserved.</div>
<div class="abs social" style="left:900px;background:#3b5b9a"></div>
<div class="abs social" style="left:927px;background:#39a8de"></div>
</body>
</html>
```